" A Quitavel é uma empresa que desenvolve e fornece o sistema de cobrança Quitavel para empresas de cobrança (escritórios de cobrança, assessorias de cobranças, escritórios de advogados), tais clientes chamamos de ASSESSORIAS, e também fornecemos o sistema para empresas que possuem uma grande quantidade de clientes inadimplentes e que fazem a cobrança destes clientes internamente através de um departamento de cobrança, estes clientes chamamos de CREDORES. Alguns clientes ASSESSORIAS: www.grupoltn-exemplo.com.br www.moraisetavares-exemplo.com.br www.rvrecupera-exemplo.com.br Alguns clientes CREDORES: www.linguaviva-exemplo.com www.grupovelarium-exemplo.com.br www.ronaldos-exemplo.com.br Todos os produtos e serviços que comercializamos são através da plataforma Quitavel, por exemplo, para que um cliente utilize nosso produto “Portal de Negociação” ele precisa contratar o Quitavel já que suas configurações são através do sistema, da mesma forma o serviço de “SMS”, já que as campanhas são criadas e disparadas pelo sistema Quitavel. O sistema Quitavel “nasceu” primeiro que a empresa Quitavel, já que dois dos atuais sócios possuíram uma empresa anterior de 2012 até a abertura da Quitavel em 1 de setembro de 2015. Esta empresa desenvolvia um sistema focado para assessorias de cobrança, porém em uma tecnologia antiga, e então resolveram criar um novo software com tecnologias atuais na época e para isto buscaram um investidor e juntos optaram por criar uma nova empresa, uma nova marca. Nossa logo foi construída através da plataforma Marca Pronta e gostamos muito do resultado! E estamos aqui novamente buscando que seus profissionais nos ajudem a criar novos materiais que hoje se fazem necessários para nós. "

```html
<!DOCTYPE html>
<html lang="pt-BR">
<head>
<meta charset="UTF-8">
<title>Os principais benefícios da plataforma Quitavel</title>
<link href="https://fonts.googleapis.com/css2?family=Montserrat:wght@600;700&family=Open+Sans:wght@400;600;700&display=swap" rel="stylesheet">
<style>
  :root {
    --bg: #eef0f3;
    --sheet: #ffffff;
    --side: #e6e8eb;
    --navy: #1d3c82;
    --blue: #2f63b3;
    --text: #5b6168;
    --line: #c9ced6;
    --shot-a: #dfe6ef;
    --shot-b: #b9c6d8;
  }
  * { box-sizing: border-box; margin: 0; padding: 0; }
  html, body { width: 1200px; height: 1200px; overflow: hidden; background: var(--bg); }
  .sheet {
    position: absolute; left: 40px; top: 220px;
    width: 1120px; height: 760px;
    background: var(--sheet);
    display: flex;
    box-shadow: 0 2px 10px rgba(0,0,0,0.08);
  }
  .gallery {
    width: 270px; background: var(--side);
    border-right: 3px solid var(--line);
    padding: 50px 30px; display: flex; flex-direction: column; gap: 40px;
  }
  .gallery-shot {
    flex: 1; border-radius: 4px;
    background: linear-gradient(160deg, var(--shot-a), var(--shot-b));
  }
  .content { flex: 1; padding: 44px 50px 30px; position: relative; font-family: "Open Sans", sans-serif; }
  .headline {
    font-family: "Montserrat", sans-serif; font-weight: 700;
    font-size: 27px; color: var(--navy); letter-spacing: 0.5px;
    text-align: center; margin: 14px 0 34px; padding-right: 120px;
  }
  .device-art {
    position: absolute; top: 30px; right: 50px; width: 110px; height: 76px;
    border-radius: 4px;
    background: linear-gradient(160deg, #f3f5f8, #c4ccd8);
  }
  .benefit { margin-bottom: 20px; }
  .benefit-title {
    font-family: "Montserrat", sans-serif; font-weight: 700;
    font-size: 15px; color: var(--blue); text-transform: uppercase; margin-bottom: 6px;
  }
  .benefit-text { font-size: 12.5px; line-height: 1.6; color: var(--text); text-align: justify; }
  .benefit-text strong { color: #3c4249; font-weight: 700; }
</style>
</head>
<body>
  <main class="sheet">
    <aside class="gallery">
      <div class="gallery-shot" role="img" aria-label="Tela do sistema Quitavel em um monitor"></div>
      <div class="gallery-shot" role="img" aria-label="Painel com gráficos circulares do sistema Quitavel"></div>
      <div class="gallery-shot" role="img" aria-label="Ambiente de escritório com computadores"></div>
    </aside>
    <section class="content">
      <div class="device-art" role="img" aria-label="Monitor exibindo a plataforma Quitavel"></div>
      <h1 class="headline">OS PRINCIPAIS BENEFÍCIOS DA PLATAFORMA</h1>

      <article class="benefit">
        <h2 class="benefit-title">Menos custos com infraestrutura</h2>
        <p class="benefit-text">O custo para manter um sistema hospedado dentro da empresa vai além do custo com os equipamentos, existem custos de licenças de software do sistema operacional, banco de dados, antivírus e outros aplicativos normalmente necessários. Envolve também custos com profissionais de TI para configuração e manutenção dos servidores e se sua empresa precisa de acesso externo pode contar com mais custos com links de internet maiores e profissionais de segurança para implantar uma política adequada. Ao colocar tudo na ponta do lápis, não se assuste!</p>
      </article>

      <article class="benefit">
        <h2 class="benefit-title">Mais disponibilidade</h2>
        <p class="benefit-text">Nossos servidores possuem disponibilidade de 99,95% garantida pelo contrato de nível de serviço (SLA) com a NuvemPrime. Além disso, para a maioria dos nossos serviços temos parceiros de redundância à disposição caso algum apresente problemas. Por exemplo, se hoje sua empresa possui apenas um fornecedor de SMS e ele fica indisponível? Provavelmente terá que aguardar o serviço ser normalizado; neste exemplo, a plataforma Quitavel já identifica que um parceiro está com problemas e realiza o envio por outro fornecedor integrado.</p>
      </article>

      <article class="benefit">
        <h2 class="benefit-title">Mais produtividade</h2>
        <p class="benefit-text">No Quitavel aplicamos desde o início o conceito de <strong>usabilidade</strong> que é sinônimo de facilidade de uso. Se um produto é fácil de usar, o usuário tem maior PRODUTIVIDADE, aprende mais rápido, memoriza as operações e comete menos erros. Também não é possível falar em produtividade sem falar de <strong>automação de tarefas</strong>. Automatize sua Régua de Cobrança de maneira simples, definindo ações automáticas conforme suas estratégias de cobrança. Toda tarefa que identificamos que pode ser automatizada, nós criamos a opção de que seja agendada pelo sistema. E frequentemente são criadas novas automatizações com base nas necessidades dos nossos clientes.</p>
      </article>

      <article class="benefit">
        <h2 class="benefit-title">Mais gestão</h2>
        <p class="benefit-text">Tenha acesso rápido às informações relevantes para tomada de decisões. São diversos os <strong>Dashboards</strong> e <strong>Relatórios</strong> disponíveis através da plataforma que mostram a realidade da sua operação de cobrança. E se não for suficiente, disponibilizamos suas informações através do nosso <strong>Data warehouse</strong> para que seja possível utilizar a ferramenta de BI da sua empresa.</p>
      </article>
    </section>
  </main>
</body>
</html>
```